36 icons (inspiration provided)

General limitations:
Designs must follow the VELDA general design line

**Please refer to attached file for more reference

Target Market(s)

Business Consulting

Industry/Entity Type

Consulting

Font styles to use
Sans Serif

Colors
0255a3
ec1f27

Requirements
Must have
• Look and feel like the 4 enclosed examples. The usage is for print and web and mobile devices.
Nice to have
• The enclosed ppt. contains an inspiration for the icon. But better ideas are welcome.
Should not have
• Must be fit within the circles

```html
<!DOCTYPE html>
<html lang="en">
<head>
<meta charset="utf-8">
<title>VELDA Institute – Icon Themes</title>
<link href="https://fonts.googleapis.com/css2?family=Open+Sans:wght@400;700&display=swap" rel="stylesheet">
<style>
  :root{
    --frame:#3e2a2b;
    --brand-blue:#0255a3;
    --brand-red:#ec1f27;
    --band-start:#4f89d4;
    --band-end:#ffffff;
    --head:#4f81bd;
    --row-dark:#d0d8e8;
    --row-light:#e9edf4;
    --ink:#111111;
    --muted:#6b6b6b;
    --ph-1:#d9dde6;
  }
  html,body{margin:0;padding:0;overflow:hidden;}
  body{width:1200px;height:1200px;background:var(--frame);font-family:"Open Sans",sans-serif;position:relative;}
  .slide{position:absolute;left:0;top:185px;width:1200px;height:831px;background:#fff;}
  .band{position:absolute;left:0;top:0;width:1200px;height:145px;
    background:linear-gradient(90deg,var(--band-start) 0%,#9dbde8 45%,#dbe7f6 70%,var(--band-end) 85%);}
  .brand{position:absolute;right:40px;top:52px;display:flex;align-items:center;gap:12px;
    color:var(--brand-blue);font-weight:700;font-size:32px;line-height:1;}
  .brand-dot{width:26px;height:26px;border-radius:50%;background:var(--brand-blue);}
  .themes{position:absolute;left:42px;top:163px;width:1099px;border-collapse:separate;border-spacing:0 2px;}
  .themes th{background:var(--head);color:#fff;font-weight:700;font-size:24px;text-align:left;
    height:60px;vertical-align:top;padding:8px 11px 0;}
  .themes td{height:139px;vertical-align:top;padding:0;position:relative;}
  .themes tr:nth-child(odd) td{background:var(--row-dark);}
  .themes tr:nth-child(even) td{background:var(--row-light);}
  .col-theme{width:278px;border-right:2px solid #fff;}
  .theme-label{font-size:24px;color:var(--ink);padding:8px 11px;}
  .art{position:absolute;background:var(--ph-1);}
  .icon{position:absolute;left:583px;width:134px;height:134px;}
  .footer{position:absolute;left:0;top:803px;width:1200px;text-align:center;font-size:13.6px;color:var(--muted);}
</style>
</head>
<body>
<div class="slide">
  <div class="band"></div>
  <div class="brand">
    <span class="brand-dot"></span>
    <span class="brand-name">VELDA Institute</span>
  </div>

  <table class="themes">
    <thead><tr><th class="col-theme">Theme</th><th>Inspiration</th></tr></thead>
    <tbody>
      <tr>
        <td class="col-theme"><div class="theme-label">Objectives</div></td>
        <td>
          <div class="art" role="img" aria-label="Red and white dartboard with three blue darts in the bullseye" style="left:34px;top:2px;width:166px;height:124px;background:linear-gradient(135deg,#f4d7d8,#c7d8ee);"></div>
          <svg class="icon" style="top:0" viewBox="0 0 134 134" aria-hidden="true">
            <circle cx="67" cy="67" r="62" fill="#fff" stroke="var(--brand-blue)" stroke-width="8"/>
            <circle cx="62" cy="72" r="24" fill="none" stroke="var(--brand-red)" stroke-width="6"/>
            <circle cx="62" cy="72" r="12" fill="none" stroke="var(--brand-red)" stroke-width="5"/>
            <circle cx="62" cy="72" r="3" fill="var(--brand-red)"/>
            <path d="M62 72 L92 50" stroke="var(--brand-red)" stroke-width="4"/>
            <path d="M86 48 L96 46 L92 56 Z" fill="var(--brand-red)"/>
          </svg>
        </td>
      </tr>
      <tr>
        <td class="col-theme"><div class="theme-label">Learning</div></td>
        <td>
          <div class="art" role="img" aria-label="Silhouette of a person working on a laptop at a desk" style="left:40px;top:14px;width:114px;height:120px;background:#e2e2e2;"></div>
          <svg class="icon" style="top:2px" viewBox="0 0 134 134" aria-hidden="true">
            <circle cx="67" cy="67" r="62" fill="#fff" stroke="var(--brand-blue)" stroke-width="8"/>
            <rect x="36" y="44" width="62" height="40" rx="3" fill="none" stroke="#555" stroke-width="5"/>
            <rect x="61" y="84" width="12" height="9" fill="#555"/>
            <rect x="50" y="93" width="34" height="5" fill="#555"/>
            <path d="M56 58 L49 64 L56 70 M78 58 L85 64 L78 70 M70 56 L64 72" fill="none" stroke="#555" stroke-width="3"/>
          </svg>
        </td>
      </tr>
      <tr>
        <td class="col-theme"><div class="theme-label">Relations</div></td>
        <td>
          <div class="art" role="img" aria-label="Line drawing of three people connected in a network" style="left:37px;top:16px;width:127px;height:119px;background:#eeeeee;"></div>
          <svg class="icon" style="top:3px" viewBox="0 0 134 134" aria-hidden="true">
            <circle cx="67" cy="67" r="62" fill="#fff" stroke="var(--brand-blue)" stroke-width="8"/>
            <path d="M67 45 L50 76 L84 76 Z" fill="none" stroke="#555" stroke-width="3"/>
            <circle cx="67" cy="45" r="13" fill="#fff" stroke="#555" stroke-width="3"/>
            <circle cx="50" cy="76" r="13" fill="#fff" stroke="#555" stroke-width="3"/>
            <circle cx="84" cy="76" r="13" fill="#fff" stroke="#555" stroke-width="3"/>
          </svg>
        </td>
      </tr>
      <tr>
        <td class="col-theme"><div class="theme-label">Position</div></td>
        <td>
          <div class="art" role="img" aria-label="Hand sketching an organisation chart of linked boxes" style="left:40px;top:13px;width:230px;height:112px;background:linear-gradient(135deg,#f2f2f2,#e2dcd3);"></div>
          <svg class="icon" style="top:4px" viewBox="0 0 134 134" aria-hidden="true">
            <circle cx="67" cy="67" r="62" fill="#fff" stroke="var(--brand-blue)" stroke-width="8"/>
          </svg>
        </td>
      </tr>
    </tbody>
  </table>

  <div class="footer">We believe there is a best practice for accelerating change in organisations and doing it repeatedly</div>
</div>
</body>
</html>
```